Marketing Brochure design required by Video Production company

We are looking for a slick, professional and eye-catching design for a marketing brochure that will showcase our company and its services.

Purpose:
The purpose of the brochure is to show our company as experienced, capable, professional and creative.

The Brochure:
The brochure will be 10 pages (including front and back cover), designed for printing in measurements of 16cm (height) x 18cm (wide).

Attached you will find:

1. Brochure Copy/Text - this is all the text to be included in the brochure. Text in red colour is not to be included in the design but is there as a guide to assist in the design

2. Design assets - our logo and hi-resolution images to be included in the design. The filenames of the images correspond with pages in the Brochure Copy/Text (as you will see)
* this does not seem to be attaching here in ArtMarketHub. Please download this file from stashbin here: https://www.stashbin.net/s/qk4tr7wnz2lpa0e/Product_Marketing_Brochure_Assets-2016-02-07.zip?dl=0

Design:
We would like the design to be open - not cramped or squashed in. Use of space is good. We want it to look very professional, but creative. And also feel simple and easy to read.

Colours to use - blues with black & white (black & white is our brand).

Please feel free to ask any questions you might have.

Thank you.

Industry/Entity Type

It Company

Font styles to use
Sans Serif

Colors
0592cd
3176b5
3276b5
33a6d7
85cae6
cee9f5
85acd3
eaf1f7

Requirements
Must have
• As per the description.
• Download design assets from:
• https://www.stashbin.net/s/qk4tr7wnz2lpa0e/Product_Marketing_Brochure_Assets-2016-02-07.zip?dl=0

```html
<!DOCTYPE html>
<html lang="en">
<head>
<meta charset="utf-8">
<title>Brochure Spread – Your Story &amp; Your Event</title>
<link href="https://fonts.googleapis.com/css2?family=Open+Sans:wght@300;400;700&display=swap" rel="stylesheet">
<style>
  :root {
    --bg: #e4e4e4;
    --white: #ffffff;
    --brand-blue: #1689c1;
    --ink-blue: #1a86c2;
    --story-dark: #3a2a22;
    --story-warm: #a7765a;
    --event-dark: #1a1230;
    --event-violet: #5b3f8f;
  }
  * { box-sizing: border-box; margin: 0; padding: 0; }
  html, body {
    width: 1200px; height: 960px; overflow: hidden;
    background: var(--bg);
    font-family: "Open Sans", Arial, sans-serif;
  }
  .stage { position: relative; width: 1200px; height: 960px; }
  .spread {
    position: absolute; left: 30px; top: 226px;
    width: 1367px; height: 608px;
    transform: scale(0.834); transform-origin: 0 0;
    display: flex;
  }
  .page {
    position: relative; width: 683.5px; height: 608px;
    text-align: center;
  }
  .page--story { background: var(--white); color: var(--ink-blue); }
  .page--event { background: var(--brand-blue); color: var(--white); }

  .kicker {
    position: absolute; top: 40px; left: 0; right: 0;
    font-weight: 700; font-size: 14px; letter-spacing: 0.2px;
  }
  .kicker span {
    display: inline-block; padding-bottom: 4px;
    border-bottom: 3px solid currentColor;
  }
  .title {
    position: absolute; top: 88px; left: 0; right: 0;
    font-weight: 300; font-size: 29px; letter-spacing: -0.3px;
  }
  .intro {
    position: absolute; top: 137px; left: 60px; right: 60px;
    font-size: 11.3px; line-height: 13.7px;
  }
  .intro p + p { margin-top: 13.7px; }
  .intro .caps { text-transform: uppercase; }

  .band {
    position: absolute; top: 261px; left: 0; right: 0; height: 136px;
  }
  .band--story { background: linear-gradient(90deg, var(--story-dark), var(--story-warm) 35%, #6b5447 60%, var(--story-warm) 80%, var(--story-dark)); }
  .band--event { background: linear-gradient(90deg, #14121a, var(--event-violet) 45%, #6a4a8c 55%, #3b2418 85%, #120c08); }

  .play {
    position: absolute; top: 244px; left: 50%;
    width: 36px; height: 36px; margin-left: -18px;
  }

  .package {
    position: absolute; left: 40px; right: 40px;
  }
  .page--story .package { top: 423px; }
  .page--event .package { top: 420px; }
  .package h3 {
    font-weight: 300; font-size: 18.5px; margin-bottom: 12px;
    text-transform: uppercase;
  }
  .package ul { list-style: none; font-size: 11.3px; line-height: 13.7px; }
  .package li::before { content: "• "; }
  .package .note { margin-top: 13.7px; font-size: 11.3px; line-height: 13.7px; }
</style>
</head>
<body>
<div class="stage">
  <div class="spread">

    <section class="page page--story">
      <div class="kicker"><span>YOUR STORY</span></div>
      <h2 class="title">VIDEO PROFILE</h2>
      <div class="intro">
        <p>The Your STORY video profile is a combination of interviews and overlay footage designed<br>to tell your business’ story. This style of video content helps your audience better understand:</p>
        <p class="caps">• What makes you unique • Why they should trust you<br>• What your product offering is and how it works • What your process is</p>
        <p>We’ll work with you to develop the best approach to deliver this in a sharp &amp; engaging fashion.</p>
      </div>
      <div class="band band--story" role="img" aria-label="Mosaic of interview portraits of business people speaking to camera"></div>
      <svg class="play" viewBox="0 0 36 36" aria-hidden="true">
        <circle cx="18" cy="18" r="16.5" fill="var(--white)" stroke="var(--brand-blue)" stroke-width="3"/>
        <circle cx="18" cy="18" r="11" fill="none" stroke="var(--brand-blue)" stroke-width="2"/>
        <path d="M15 12.5 L23.5 18 L15 23.5 Z" fill="var(--brand-blue)"/>
      </svg>
      <div class="package">
        <h3>The package includes:</h3>
        <ul>
          <li>Filming of interviews + overlay footage at your desired location</li>
          <li>A slick, professionally edited high definition video</li>
          <li>Quick turnaround time and review process</li>
          <li>An opportunity to make any changes before your video is finalised</li>
          <li>Delivery in your choice of formats</li>
        </ul>
        <p class="note">Have additional requirements?<br>No problem. Contact us to discuss a quote.</p>
      </div>
    </section>

    <section class="page page--event">
      <div class="kicker"><span>YOUR EVENT</span></div>
      <h2 class="title">EVENT COVERAGE &amp; HIGHLIGHTS</h2>
      <div class="intro">
        <p>Got a launch, seminar, celebration, party or any other event that you want filmed?<br>We’ve got you covered. The Your EVENT package provides creative<br>event coverage, with the best parts of your event condensed into a slick highlights<br>video that captures the vibe and essence of your event.</p>
      </div>
      <div class="band band--event" role="img" aria-label="Event photos: speakers on stage, guests dancing under purple lights, performers at a night party"></div>
      <svg class="play" viewBox="0 0 36 36" aria-hidden="true">
        <circle cx="18" cy="18" r="16.5" fill="var(--white)" stroke="var(--brand-blue)" stroke-width="3"/>
        <circle cx="18" cy="18" r="11" fill="none" stroke="var(--brand-blue)" stroke-width="2"/>
        <path d="M15 12.5 L23.5 18 L15 23.5 Z" fill="var(--brand-blue)"/>
      </svg>
      <div class="package">
        <h3>The package includes:</h3>
        <ul>
          <li>Filming of your event exactly as you need</li>
          <li>A slick, professionally edited high definition video, cut to music to suit your event</li>
          <li>An opportunity to review an edit and make changes before your video is finalised</li>
          <li>Delivery in your choice of formats</li>
          <li>Speech &amp; speaker recording also available</li>
        </ul>
        <p class="note">Have additional requirements?<br>No problem. Contact us to discuss a quote.</p>
      </div>
    </section>

  </div>
</div>
</body>
</html>
```